Business card for IT company

Looking for a business card for an IT company providing server, network, and application support to medium businesses. Company name is Calderwick Systems. Website is www.calderwicksystems.example, would like to use the green color that is on the homepage. Prefer design to be done in Illustrator. Please, only DESIGNERS apply - no PHP programmers attempting to do design. Thank you

Industry/Entity Type

Information Technology

Requirements
Must have
• Green
Should not have
• Template designs, or designs done by non-designer type people

```html
<!DOCTYPE html>
<html lang="en">
<head>
<meta charset="utf-8">
<title>Calderwick Systems – Business Card</title>
<link rel="stylesheet" href="https://fonts.googleapis.com/css2?family=Open+Sans:wght@300;400;600;700&display=swap">
<style>
  :root {
    --green: #7fb23a;
    --green-dark: #5e9424;
    --green-light: #a6cf63;
    --ink: #222222;
    --muted: #6b6b6b;
    --paper: #ffffff;
    --backdrop: #ecebe7;
  }
  * { box-sizing: border-box; margin: 0; padding: 0; }
  html, body { width: 771px; height: 1200px; overflow: hidden; }
  body {
    background: var(--backdrop);
    font-family: "Open Sans", Arial, sans-serif;
    display: flex;
    flex-direction: column;
    align-items: center;
    justify-content: center;
    gap: 70px;
  }
  .card {
    width: 660px;
    height: 377px;
    position: relative;
    box-shadow: 0 4px 18px rgba(0,0,0,.12);
    overflow: hidden;
  }

  /* Brand lockup: plain circle + name */
  .brand { display: flex; flex-direction: column; align-items: center; }
  .brand-mark { width: 110px; height: 110px; border-radius: 50%; }
  .brand-name {
    margin-top: 18px;
    font-weight: 300;
    font-size: 30px;
    letter-spacing: 2px;
    line-height: 1.05;
    text-align: center;
    text-transform: uppercase;
  }
  .brand-rule { width: 210px; height: 1px; margin-top: 10px; }

  /* Front */
  .card-front { background: var(--paper); }
  .card-front .brand { position: absolute; left: 50px; top: 92px; }
  .card-front .brand-mark { background: var(--green-light); }
  .card-front .brand-name { color: var(--green); }
  .card-front .brand-rule { background: var(--green); }

  .contact { position: absolute; left: 340px; top: 102px; }
  .person-name { font-size: 30px; font-weight: 400; color: var(--ink); }
  .person-title { font-size: 15px; color: var(--green); margin-top: 2px; }
  .contact-list { list-style: none; margin-top: 26px; }
  .contact-list li {
    display: flex; align-items: center; gap: 14px;
    font-size: 15px; color: var(--ink); margin-bottom: 14px;
  }
  .contact-list svg { width: 14px; height: 14px; flex: none; }

  /* Back */
  .card-back {
    background: linear-gradient(160deg, var(--green-light) 0%, var(--green) 45%, var(--green-dark) 100%);
    color: var(--paper);
  }
  .card-back .brand { position: absolute; left: 60px; top: 28px; }
  .card-back .brand-mark { width: 78px; height: 78px; border: 3px solid var(--paper); }
  .card-back .brand-name { font-size: 22px; margin-top: 12px; }
  .card-back .brand-rule { background: var(--paper); width: 170px; margin-top: 8px; }

  .tagline {
    position: absolute; left: 60px; right: 40px; top: 188px;
    font-size: 14px; line-height: 1.4; font-weight: 400;
  }
  .services {
    position: absolute; left: 60px; right: 40px; bottom: 22px;
    display: flex; justify-content: space-between;
  }
  .service { width: 170px; }
  .service svg { width: 28px; height: 28px; display: block; margin-bottom: 5px; }
  .service-name { font-size: 14px; font-weight: 700; color: rgba(255,255,255,.95); }
  .service-desc { font-size: 9px; line-height: 1.35; color: rgba(255,255,255,.8); margin-top: 3px; }
</style>
</head>
<body>

  <section class="card card-front" aria-label="Card front">
    <div class="brand">
      <div class="brand-mark"></div>
      <div class="brand-name">Calderwick<br>Systems</div>
      <div class="brand-rule"></div>
    </div>

    <div class="contact">
      <h1 class="person-name">Your Name</h1>
      <p class="person-title">Job Title</p>
      <ul class="contact-list">
        <li>
          <svg viewBox="0 0 14 14" aria-hidden="true"><path fill="var(--green)" d="M3 1h2l1 3-1.5 1a7 7 0 0 0 4.5 4.5L10 8l3 1v2a2 2 0 0 1-2 2A10 10 0 0 1 1 3a2 2 0 0 1 2-2z"/></svg>
          555.010.0142
        </li>
        <li>
          <svg viewBox="0 0 14 14" aria-hidden="true"><rect x="1" y="3" width="12" height="8" rx="1" fill="var(--green)"/><path d="M1.5 3.5 7 8l5.5-4.5" stroke="#fff" fill="none" stroke-width="1"/></svg>
          support@calderwicksystems.example
        </li>
        <li>
          <svg viewBox="0 0 14 14" aria-hidden="true"><circle cx="7" cy="7" r="6" fill="none" stroke="var(--green)" stroke-width="1.3"/><path d="M1 7h12M7 1c-3 3-3 9 0 12M7 1c3 3 3 9 0 12" stroke="var(--green)" fill="none" stroke-width="1"/></svg>
          www.calderwicksystems.example
        </li>
      </ul>
    </div>
  </section>

  <section class="card card-back" aria-label="Card back">
    <div class="brand">
      <div class="brand-mark"></div>
      <div class="brand-name">Calderwick<br>Systems</div>
      <div class="brand-rule"></div>
    </div>

    <p class="tagline">We Provide a complete range of IT services, from disaster recovery to infrastructure expansion. Our goal is to keep your business running smoothly without hiccups.</p>

    <div class="services">
      <div class="service">
        <svg viewBox="0 0 30 30" aria-hidden="true"><g fill="none" stroke="rgba(255,255,255,.85)" stroke-width="1.6"><rect x="3" y="5" width="24" height="6"/><rect x="3" y="12" width="24" height="6"/><rect x="3" y="19" width="24" height="6"/></g></svg>
        <div class="service-name">Networking</div>
        <div class="service-desc">Routers, switches, firewalls, wireless and everything else that connects</div>
      </div>
      <div class="service">
        <svg viewBox="0 0 30 30" aria-hidden="true"><rect x="4" y="4" width="22" height="22" fill="rgba(255,255,255,.85)"/></svg>
        <div class="service-name">Server Suite</div>
        <div class="service-desc">Directory, mail, clustering, file services and others</div>
      </div>
      <div class="service">
        <svg viewBox="0 0 30 30" aria-hidden="true"><g fill="rgba(255,255,255,.85)"><ellipse cx="15" cy="6" rx="10" ry="3.5"/><path d="M5 9c0 2 4.5 3.5 10 3.5S25 11 25 9v5c0 2-4.5 3.5-10 3.5S5 16 5 14z"/><path d="M5 18c0 2 4.5 3.5 10 3.5S25 20 25 18v5c0 2-4.5 3.5-10 3.5S5 25 5 23z"/></g></svg>
        <div class="service-name">Databases</div>
        <div class="service-desc">SQL setup, tuning, backups and replication</div>
      </div>
    </div>
  </section>

</body>
</html>
```